Quirky Paris documentary film needs a poster

I'm making a quirky documentary about how I've seen too many romantic comedies so I've moved to Paris to try to turn my life into a rom-com. It's called "The Freckled Tourist On Loan." I've included a few sample stills, or the whole thing could be an illustration. The film is full of references to other films like Clotilde, Rain On Dovecote Lane, Delphina, so you could riff of of their posters. 27" x 41"

Industry/Entity Type

Film Production

Font styles to use
Sans Serif

Requirements
Must have
• It should say "From the director of Seeking Tuesday" "Oosterdonk Films Presents" "Directed by Dennis R. Colwell" and at the bottom it should have the website: thefreckledtouristonloan.example
Nice to have
• You could possibly include this text:
• What happens when you've seen too many romantic comedies?
• You move to Paris and try to turn your life into one.

```html
<!DOCTYPE html>
<html lang="en">
<head>
<meta charset="utf-8">
<title>The Freckled Tourist On Loan — Poster</title>
<link rel="stylesheet" href="https://fonts.googleapis.com/css2?family=Montserrat:wght@200;400;500;700;800&family=Oswald:wght@600&display=swap">
<style>
  :root {
    --ink: #17161f;
    --white: #ffffff;
    --paper-edge: #d9d9dc;
    --paper-mid: #f1f1f2;
    --violet: #8a6fb3;
    --lilac: #b49ad6;
    --rose: #e79ab9;
    --peach: #f3b6bf;
    --steel: #6f8cb3;
  }
  html, body {
    margin: 0;
    padding: 0;
    overflow: hidden;
    background: var(--white);
  }
  .poster {
    position: relative;
    width: 790px;
    height: 1200px;
    overflow: hidden;
    font-family: "Montserrat", sans-serif;
    color: var(--ink);
    background: radial-gradient(ellipse 62% 55% at 50% 50%, var(--white) 0%, var(--paper-mid) 60%, var(--paper-edge) 100%);
  }
  .director-credit {
    position: absolute;
    top: 62px;
    left: 0;
    width: 100%;
    text-align: center;
    font-size: 12.5px;
    font-weight: 500;
    letter-spacing: 1.6px;
    text-transform: uppercase;
  }
  .director-credit strong { font-weight: 800; }
  .tagline {
    position: absolute;
    top: 112px;
    left: 0;
    width: 100%;
    text-align: center;
    font-size: 20px;
    font-weight: 400;
    line-height: 1.2;
    letter-spacing: 0.6px;
    text-transform: uppercase;
  }
  .tagline strong { font-weight: 800; }
  .portrait {
    position: absolute;
    top: 0;
    left: 0;
    width: 790px;
    height: 1200px;
  }
  .presenter {
    position: absolute;
    top: 702px;
    left: 0;
    width: 100%;
    text-align: center;
    color: var(--white);
    font-weight: 700;
    font-size: 12.5px;
    letter-spacing: 1.2px;
    text-transform: uppercase;
    line-height: 1.25;
  }
  .presenter small {
    display: block;
    font-weight: 400;
    font-size: 8.5px;
    letter-spacing: 1.4px;
  }
  .title {
    position: absolute;
    top: 742px;
    left: 0;
    width: 100%;
    margin: 0;
    text-align: center;
    color: var(--white);
    text-transform: uppercase;
    line-height: 0.98;
    text-shadow: 0 0 14px rgba(90, 60, 120, 0.25);
  }
  .title span { display: block; }
  .title .thin { font-weight: 200; }
  .title .lead { font-size: 62px; font-weight: 200; letter-spacing: 4px; }
  .title .line-one { font-size: 70px; font-weight: 800; letter-spacing: 1px; }
  .title .line-two { font-size: 66px; font-weight: 800; letter-spacing: 0px; white-space: nowrap; }
  .director {
    position: absolute;
    top: 958px;
    left: 0;
    width: 100%;
    text-align: center;
    color: var(--white);
    font-size: 12px;
    font-weight: 400;
    letter-spacing: 2px;
    text-transform: uppercase;
  }
  .director strong { font-weight: 800; }
  .release {
    position: absolute;
    top: 1146px;
    left: 0;
    width: 100%;
    text-align: center;
    color: var(--white);
    font-family: "Oswald", sans-serif;
    font-weight: 600;
    font-size: 21px;
    line-height: 1;
    text-transform: uppercase;
    text-shadow: 0 0 6px rgba(0, 0, 0, 0.35);
  }
  .release .site {
    display: block;
    margin-top: 3px;
    font-family: "Montserrat", sans-serif;
    font-size: 9px;
    font-weight: 700;
    letter-spacing: 0.3px;
  }
</style>
</head>
<body>
<main class="poster">
  <p class="director-credit">From the director of <strong>Seeking Tuesday</strong></p>
  <p class="tagline">&ldquo;What happens<br>when you&rsquo;ve <strong>seen too many<br>romantic comedies?&rdquo;</strong></p>

  <svg class="portrait" viewBox="0 0 790 1200" role="img" aria-label="Head-and-shoulders silhouette of the filmmaker filled with a violet and pink Paris sky, the Eiffel Tower and a rooftop skyline">
    <defs>
      <linearGradient id="sky" x1="0" y1="0" x2="0" y2="1">
        <stop offset="0" stop-color="var(--violet)"/>
        <stop offset="0.35" stop-color="var(--lilac)"/>
        <stop offset="0.62" stop-color="var(--rose)"/>
        <stop offset="0.78" stop-color="var(--peach)"/>
        <stop offset="0.86" stop-color="var(--steel)"/>
        <stop offset="1" stop-color="var(--steel)"/>
      </linearGradient>
      <linearGradient id="fade" x1="0" y1="0" x2="0" y2="1">
        <stop offset="0.85" stop-color="#fff"/>
        <stop offset="0.95" stop-color="#000"/>
      </linearGradient>
      <mask id="fade-out">
        <rect x="0" y="0" width="790" height="1200" fill="url(#fade)"/>
      </mask>
    </defs>
    <path mask="url(#fade-out)" fill="url(#sky)"
      d="M300 232 C350 212 470 214 520 238 C575 266 612 330 618 420
         C624 480 626 520 618 560 C610 610 590 660 565 700
         C620 720 700 760 790 850 L790 1140 L0 1140 L0 850
         C80 770 160 725 225 700
         C200 660 180 610 170 560 C160 500 170 440 185 390
         C205 320 245 258 300 232 Z"/>
  </svg>

  <p class="presenter">Oosterdonk Films<small>Presents</small></p>
  <h1 class="title">
    <span class="lead">The</span>
    <span class="line-one">Freckled</span>
    <span class="line-two">Tourist <span class="thin" style="display:inline">On</span> Loan</span>
  </h1>
  <p class="director">Directed by <strong>Dennis R. Colwell</strong></p>

  <p class="release">Coming soon<span class="site">thefreckledtouristonloan.example</span></p>
</main>
</body>
</html>
```